Business card and stationary for Intellectual Property Consultant & Law Firm
Harborline Claims Omniworks
Business card and stationary for Intellectual Property Consultant & Law Firm - Law
Creative Brief
Simple
Dorin Makalesu
President Director
Kelor Business Center 11th Floor Jl. Raya Wibisana Kav.37-38 Jakarta Pusat 10485, Indonesia
office@harborlineclaims.example
www.harborlineclaims.example
Member: OQRU, EKLM, UVBO, WDGF
Please add Intellectual Property Rights Consultant & Law Firm for letterhead additional of our email : hbl42@harborlineclaims.example; marks@harborlineclaims.example
please add Branch office : Surabaya (+6231) 480 3926 Medan (+6261) 819 4057 Solo (+62271) 634 918
trelvorin trelvorin
Dear All, Please provide me the stationary : letterhead, envelope, cds, ballpoint, ruler, stamps, usb sticks etc
dunmoral dunmoral
Please upload Ai or eps file of your logo thankyou
Please add : Intellectual Property Rights Consultant & Law Firm in envelope and letter head.

```html
<!DOCTYPE html>
<html lang="en">
<head>
<meta charset="utf-8">
<title>Harborline Claims Omniworks – Business Card</title>
<link rel="stylesheet" href="https://fonts.googleapis.com/css2?family=Poppins:ital,wght@0,400;0,500;0,600;1,400&display=swap">
<style>
  :root {
    --backdrop: #d6d7d9;
    --paper: #ffffff;
    --navy: #0f2646;
    --ink: #1c2f52;
    --text-grey: #555a61;
    --logo-grey: #5b5f66;
    --logo-light: #c9ccd2;
    --amber: #efa52c;
    --band-grey: #c7c9cc;
  }
  * { box-sizing: border-box; margin: 0; padding: 0; }
  html, body { width: 1200px; height: 878px; overflow: hidden; }
  body {
    background: var(--backdrop);
    font-family: "Poppins", sans-serif;
    position: relative;
  }
  .card {
    position: absolute;
    left: 290px;
    width: 620px;
    height: 354px;
    border-radius: 4px;
    overflow: hidden;
    box-shadow: 0 6px 18px rgba(0,0,0,.18);
  }
  /* back side */
  .card-back { top: 68px; background: var(--navy); }
  .card-back .brand {
    position: absolute;
    left: 0; right: 0; top: 128px;
    text-align: center;
    color: var(--logo-light);
    font-weight: 500;
    font-size: 34px;
    line-height: 1.1;
    letter-spacing: .5px;
  }
  .card-back .brand small {
    display: block;
    font-size: 34px;
  }
  /* front side */
  .card-front { top: 456px; background: var(--paper); }
  .card-front .brand {
    position: absolute;
    left: 34px; top: 34px;
    display: flex; align-items: flex-start; gap: 10px;
    color: var(--logo-grey);
    font-weight: 500;
    font-size: 30px;
    line-height: 1.05;
  }
  .brand-dot {
    width: 14px; height: 14px;
    background: var(--amber);
    margin-top: 9px;
    flex: none;
  }
  .contact {
    position: absolute;
    left: 356px; top: 138px;
    color: var(--text-grey);
    font-size: 12px;
    line-height: 1.45;
  }
  .contact .person {
    color: var(--ink);
    font-weight: 600;
    font-size: 17px;
    line-height: 1.1;
  }
  .contact .role {
    color: var(--amber);
    font-style: italic;
    font-size: 12px;
    margin-bottom: 10px;
  }
  .contact .address { margin-bottom: 10px; }
  .contact ul { list-style: none; }
  .contact li { display: flex; align-items: center; gap: 8px; }
  .contact li svg { width: 10px; height: 10px; fill: var(--amber); flex: none; }
  .footer-band { position: absolute; left: 0; bottom: 0; width: 620px; height: 46px; }
  .website {
    position: absolute;
    left: 216px; bottom: 14px;
    color: #fff;
    font-size: 12px;
    letter-spacing: .4px;
  }
</style>
</head>
<body>

<section class="card card-back" aria-label="Card back">
  <div class="brand">Harborline Claims<small>Omniworks</small></div>
</section>

<section class="card card-front" aria-label="Card front">
  <div class="brand">
    <span class="brand-dot"></span>
    <span>Harborline<br>Claims<br>Omniworks</span>
  </div>

  <div class="contact">
    <p class="person">John Smithson</p>
    <p class="role">Managing Director</p>
    <p class="address">P.O Box Mailwaill St<br>Sample City Country 324</p>
    <ul>
      <li><svg viewBox="0 0 10 10"><path d="M2 0h2l1 3-1.5 1a6 6 0 0 0 2.5 2.5L7 5l3 1v2a2 2 0 0 1-2 2A8 8 0 0 1 0 2a2 2 0 0 1 2-2z"/></svg>123 456 7890</li>
      <li><svg viewBox="0 0 10 10"><path d="M1 0h6v3H1zM0 4h10v6H0z"/></svg>123 456 7890</li>
      <li><svg viewBox="0 0 10 10"><path d="M2 0h6v10H2z"/></svg>123 456 7890</li>
      <li><svg viewBox="0 0 10 10"><path d="M0 2h10v6H0z"/></svg>yourname@example.org</li>
    </ul>
  </div>

  <svg class="footer-band" viewBox="0 0 620 46" preserveAspectRatio="none" aria-hidden="true">
    <polygon points="0,20 190,20 170,46 0,46" fill="var(--band-grey)"/>
    <polygon points="200,0 620,0 620,46 170,46" fill="var(--amber)"/>
  </svg>
  <p class="website">www.yourwebsitename.example</p>
</section>

</body>
</html>
```